Bramble Peak Information Technology Business Card
Services for Move Add Change, Technical Relocation, Server Room Support, Technical Support
Bramble Peak Information Technology Business Card - Information Technology
Creative Brief
Professional
Owen Darlisk
2917 41st Lane Northeast Seattle WA 98422
owen@bramblepkit-example.com
www.bramblepkit-example.com
The original logo on the back, #34 and #35
Move Add and Changes, Corporate Relocation, Server Room Support, Technical Support

```html
<!DOCTYPE html>
<html lang="en">
<head>
<meta charset="utf-8">
<title>Bramble Peak Information Technology — Stationery</title>
<link href="https://fonts.googleapis.com/css2?family=Montserrat:wght@800&family=Open+Sans:wght@400;600&display=swap" rel="stylesheet">
<style>
  :root {
    --bg: #eef0f1;
    --paper: #ffffff;
    --charcoal: #3a3a3c;
    --orange: #f39a1e;
    --ink: #555557;
    --muted: #9a9a9c;
  }
  * { margin: 0; padding: 0; box-sizing: border-box; }
  html, body { width: 1200px; height: 937px; overflow: hidden; background: var(--bg); }
  body { position: relative; font-family: "Open Sans", sans-serif; color: var(--ink); }

  .sheet { position: absolute; background: var(--paper); overflow: hidden; }
  .sheet > svg.edge { position: absolute; top: 0; right: 0; height: 100%; }

  .wordmark {
    font-family: "Montserrat", sans-serif; font-weight: 800;
    color: var(--charcoal); letter-spacing: 0.5px; white-space: nowrap;
    display: flex; align-items: center; gap: 0.35em;
  }
  .wordmark .dot { width: 0.5em; height: 0.5em; border-radius: 50%; background: var(--orange); }

  /* Letterhead */
  .letterhead { left: 182px; top: 66px; width: 396px; height: 542px; }
  .letterhead .wordmark { position: absolute; left: 34px; top: 46px; font-size: 20px; }
  .letter-body { position: absolute; left: 34px; top: 112px; width: 236px; font-size: 5.4px; line-height: 1.6; }
  .letter-body p { margin-bottom: 7px; }
  .signature { width: 40px; height: 14px; background: #e4e4e6; margin: 4px 0 5px; }
  .letter-foot { position: absolute; left: 34px; bottom: 42px; font-size: 5px; line-height: 1.7; }
  .letter-foot .name { font-weight: 600; color: var(--charcoal); }

  /* Folder */
  .folder { left: 633px; top: 38px; width: 435px; height: 577px; }
  .folder .wordmark { position: absolute; left: 64px; top: 268px; font-size: 28px; }

  /* Business cards */
  .card { left: 46px; width: 187px; height: 112px; border-radius: 8px; }
  .card-front { top: 656px; }
  .card-front .wordmark { position: absolute; left: 8px; top: 50px; font-size: 8px; letter-spacing: 0.2px; }
  .card-front .panel { position: absolute; right: 0; top: 0; width: 100px; height: 100%; background: var(--charcoal); border-radius: 0 8px 8px 0; color: #fff; padding: 14px 5px 0 11px; font-size: 4.6px; line-height: 1.8; }
  .card-front .panel::before { content: ""; position: absolute; left: 0; top: 0; width: 4px; height: 100%; background: var(--orange); }
  .card-front .panel .name { font-weight: 600; font-size: 6px; }
  .card-front .contact { margin-top: 8px; }
  .card-back { top: 792px; }
  .card-back .wordmark { position: absolute; left: 0; right: 0; top: 46px; justify-content: center; font-size: 15px; }

  /* Envelopes */
  .envelope-front { left: 253px; top: 671px; width: 446px; height: 213px; }
  .envelope-front .wordmark { position: absolute; left: 24px; top: 32px; font-size: 16px; }
  .envelope-back { left: 737px; top: 671px; width: 418px; height: 213px; }
  .envelope-back svg { position: absolute; inset: 0; }
  .envelope-back .site { position: absolute; left: 0; right: 0; top: 22px; text-align: center; color: #fff; font-size: 11px; letter-spacing: 2px; }
</style>
</head>
<body>

  <section class="sheet letterhead">
    <div class="wordmark"><span>BRAMBLE PEAK</span><span class="dot"></span></div>
    <div class="letter-body">
      <p>July 4, 2024</p>
      <p>Dear Client,<br>Office 12, Building 4, Seattle</p>
      <p>We are glad to confirm our plan for your office move. Our team will handle every desk, cable and server so your staff can keep working without delay.</p>
      <p>Please review the attached schedule and let us know of any change.</p>
      <p>We look forward to a smooth relocation and lasting support for your technical needs in the months ahead.</p>
      <p>Kind regards,</p>
      <div class="signature" role="img" aria-label="Handwritten signature"></div>
      <p>Owen Darlisk<br>Director</p>
    </div>
    <div class="letter-foot">
      <div class="name">Bramble Peak Information Technology</div>
      <div>2917 41st Lane Northeast, Seattle WA 98422</div>
      <div>+1 206 555 0142</div>
      <div>owen@bramblepkit-example.com</div>
      <div>www.bramblepkit-example.com</div>
    </div>
    <svg class="edge" viewBox="0 0 80 542" width="80" preserveAspectRatio="none" aria-hidden="true">
      <path d="M40 0 Q8 271 40 542 L80 542 L80 0 Z" fill="var(--charcoal)"/>
      <path d="M30 0 Q-4 271 30 542" fill="none" stroke="var(--orange)" stroke-width="3"/>
    </svg>
  </section>

  <section class="sheet folder">
    <div class="wordmark"><span>BRAMBLE PEAK</span><span class="dot"></span></div>
    <svg class="edge" viewBox="0 0 80 577" width="80" preserveAspectRatio="none" aria-hidden="true">
      <path d="M42 0 Q6 288 42 577 L80 577 L80 0 Z" fill="var(--charcoal)"/>
      <path d="M32 0 Q-6 288 32 577" fill="none" stroke="var(--orange)" stroke-width="3.5"/>
    </svg>
  </section>

  <section class="sheet card card-front">
    <div class="wordmark"><span>BRAMBLE PEAK</span></div>
    <div class="panel">
      <div class="name">Owen Darlisk</div>
      <div>Director</div>
      <div class="contact">
        <div>+1 206 555 0142</div>
        <div>owen@bramblepkit-example.com</div>
        <div>www.bramblepkit-example.com</div>
        <div>2917 41st Lane Northeast, 98422</div>
      </div>
    </div>
  </section>

  <section class="sheet card card-back">
    <div class="wordmark"><span>BRAMBLE PEAK</span><span class="dot"></span></div>
  </section>

  <section class="sheet envelope-front">
    <div class="wordmark"><span>BRAMBLE PEAK</span><span class="dot"></span></div>
    <svg class="edge" viewBox="0 0 70 213" width="70" preserveAspectRatio="none" aria-hidden="true">
      <path d="M40 0 Q16 106 40 213 L70 213 L70 0 Z" fill="var(--charcoal)"/>
      <path d="M30 0 Q6 106 30 213" fill="none" stroke="var(--orange)" stroke-width="3"/>
    </svg>
  </section>

  <section class="sheet envelope-back">
    <svg viewBox="0 0 418 213" width="418" height="213" aria-hidden="true">
      <path d="M0 0 H418 V40 Q209 118 0 40 Z" fill="var(--charcoal)"/>
      <path d="M0 46 Q209 124 418 46" fill="none" stroke="var(--orange)" stroke-width="3"/>
    </svg>
    <div class="site">www.bramblepkit-example.com</div>
  </section>

</body>
</html>
```